Business Card design

Keen on a very modern design with using the red star as a feature point preferably will have it printed with red foiling.

Target Market(s)

Cosmetics

Industry/Entity Type

Cosmetics

Contact Information for Business Card

Marnie Telford
Director
17 Brisbrook Lane
Wyndale Heights Victoria
Australia 3148
marnie@glowcratesupply.com.au

Font styles to use
Sans Serif

Colors
ec1f27
000000

Requirements
Must have
• Keen on some red stars on back with black background and I may get the red components printed as red foiling potentially

```html
<!DOCTYPE html>
<html lang="en">
<head>
<meta charset="utf-8">
<title>Glowcrate Business Card</title>
<link rel="stylesheet" href="https://fonts.googleapis.com/css2?family=Open+Sans:wght@400;700&family=Oswald:wght@600&display=swap">
<style>
  :root {
    --stage: #2b2b2b;
    --card: #2a2a2a;
    --card-back: #262626;
    --red: #ec1f27;
    --white: #ffffff;
    --soft-white: #e9e9e9;
    --logo-grey: #9a9a9a;
  }
  * { margin: 0; padding: 0; box-sizing: border-box; }
  html, body {
    width: 1200px; height: 1000px; overflow: hidden;
    background: var(--stage);
    font-family: "Open Sans", sans-serif;
  }
  .card {
    position: absolute; left: 270px;
    width: 660px; height: 377px;
    background: var(--card);
    box-shadow: 0 10px 30px rgba(0,0,0,.45);
  }
  .card--back { top: 70px; background: var(--card-back); }
  .card--front { top: 520px; }

  .brand {
    position: absolute; display: flex; align-items: center; gap: 10px;
    font-family: "Open Sans", sans-serif; font-weight: 700;
    letter-spacing: -1px; line-height: 1;
  }
  .brand__dot { width: 22px; height: 22px; border-radius: 50%; background: var(--red); flex: none; }
  .card--back .brand { left: 50%; top: 50%; transform: translate(-50%, -50%); font-size: 58px; color: var(--logo-grey); }
  .card--back .brand__dot { width: 30px; height: 30px; }
  .card--front .brand { right: 50px; top: 100px; font-size: 40px; color: var(--white); }

  .person { position: absolute; left: 40px; top: 40px; }
  .person__name {
    font-family: "Oswald", sans-serif; font-weight: 600;
    font-size: 32px; letter-spacing: 1px; color: var(--red);
    text-transform: uppercase; line-height: 1.05;
  }
  .person__role { font-size: 16px; color: var(--white); letter-spacing: .5px; }

  .contact { position: absolute; left: 40px; bottom: 48px; list-style: none; }
  .contact__item {
    display: flex; align-items: center; gap: 14px;
    font-size: 17px; color: var(--soft-white); line-height: 26px;
  }
  .contact__icon { width: 16px; height: 16px; flex: none; }
  .contact__highlight { color: var(--red); }

  .address {
    position: absolute; right: 50px; bottom: 40px;
    text-align: right; font-style: normal;
    font-size: 17px; line-height: 24px; color: var(--soft-white);
  }
</style>
</head>
<body>
  <section class="card card--back" aria-label="Card back">
    <div class="brand"><span class="brand__dot"></span>Glowcrate</div>
  </section>

  <section class="card card--front" aria-label="Card front">
    <div class="person">
      <h1 class="person__name">Marnie Telford</h1>
      <p class="person__role">Director</p>
    </div>

    <div class="brand"><span class="brand__dot"></span>Glowcrate</div>

    <ul class="contact">
      <li class="contact__item">
        <svg class="contact__icon" viewBox="0 0 16 16" aria-hidden="true"><path fill="#ec1f27" d="M3.5 1.5l2.5 2.8-1.4 1.8c.9 2 2.4 3.5 4.4 4.4l1.8-1.4 2.8 2.5-1.6 2.4C6.8 13.7 2.3 9.2 1.1 3.1z"/></svg>
        000 482 7516
      </li>
      <li class="contact__item">
        <svg class="contact__icon" viewBox="0 0 16 16" aria-hidden="true"><rect x="1" y="3" width="14" height="10" fill="#ec1f27"/><path d="M1 3l7 6 7-6" fill="none" stroke="#2a2a2a" stroke-width="1.3"/></svg>
        marnie@glowcratesupply.com.au
      </li>
      <li class="contact__item">
        <svg class="contact__icon" viewBox="0 0 16 16" aria-hidden="true"><g fill="none" stroke="#ec1f27" stroke-width="1.4"><circle cx="8" cy="8" r="6.5"/><ellipse cx="8" cy="8" rx="3" ry="6.5"/><path d="M1.5 8h13"/></g></svg>
        <span>www.<span class="contact__highlight">glowcratesupply</span>.com.au</span>
      </li>
    </ul>

    <address class="address">
      17 Brisbrook Lane<br>
      Wyndale Heights Victoria<br>
      Australia 3148
    </address>
  </section>
</body>
</html>
```